Business Card Design - Carrington Hill Lodge

We are looking at a new design for our business cards that has a modern and professional look. We run a residential aged care facility focussing on the care of residents. The cards will be used for potential clients, consultants and business opportunities in this sector. Blue and white is our main colours and would to see these colours incorporated in the design.
Industry/Entity Type
Business
Contact Information for Business Card
Carrington Hill Lodge, Darren Pelham, dpelham@carringtonhilllodge.com.au, Finance Manager, 0491 736 208, BCom, 48 Yarrabee Way, Wattle Downs, Qld 4215.

```html
<!DOCTYPE html>
<html lang="en">
<head>
<meta charset="utf-8">
<title>Carrington Hill Lodge – Business Card</title>
<link rel="stylesheet" href="https://fonts.googleapis.com/css2?family=Arimo:wght@400;700&display=swap">
<style>
  :root {
    --lodge-blue: #4e7891;
    --card-white: #ffffff;
    --page-bg: #ffffff;
    --card-shadow: rgba(0, 0, 0, 0.12);
  }
  * { box-sizing: border-box; margin: 0; padding: 0; }
  html, body {
    width: 703px;
    height: 1200px;
    overflow: hidden;
    background: var(--page-bg);
    font-family: "Arimo", Arial, sans-serif;
  }
  .canvas {
    position: relative;
    width: 703px;
    height: 1200px;
  }
  .card {
    position: absolute;
    left: 41px;
    width: 620px;
    height: 382px;
    background: var(--lodge-blue);
    box-shadow: 0 0 4px var(--card-shadow);
    overflow: hidden;
  }
  .card--front { top: 201px; }
  .card--back  { top: 617px; }

  .contact {
    position: absolute;
    left: 44px;
    top: 31px;
    color: var(--card-white);
    line-height: 23px;
    font-size: 15.5px;
  }
  .contact__name {
    font-weight: 700;
    font-size: 17.5px;
    margin-bottom: 1px;
  }
  .brand-band {
    position: absolute;
    left: 0;
    top: 129px;
    width: 100%;
    height: 124px;
    background: var(--card-white);
    display: flex;
    align-items: center;
    justify-content: center;
    gap: 12px;
  }
  .brand-mark {
    width: 22px;
    height: 22px;
    border-radius: 50%;
    background: var(--lodge-blue);
  }
  .brand-name {
    color: var(--lodge-blue);
    font-size: 22px;
    font-weight: 400;
    letter-spacing: 1.5px;
    text-transform: uppercase;
  }
  .address {
    position: absolute;
    left: 0;
    top: 264px;
    width: 100%;
    text-align: center;
    color: var(--card-white);
    font-size: 15px;
  }
  .back-brand {
    position: absolute;
    left: 0;
    top: 0;
    width: 100%;
    height: 100%;
    display: flex;
    align-items: center;
    justify-content: center;
    gap: 12px;
    padding-bottom: 20px;
  }
  .back-brand .brand-mark { background: var(--card-white); }
  .back-brand .brand-name { color: var(--card-white); }
</style>
</head>
<body>
  <main class="canvas">
    <section class="card card--front" aria-label="Business card front">
      <div class="contact">
        <p class="contact__name">Darren Pelham</p>
        <p class="contact__role">Finance Manager,</p>
        <p class="contact__email">dpelham@carringtonhilllodge.com.au</p>
        <p class="contact__phone">0491 736 208</p>
      </div>
      <div class="brand-band">
        <span class="brand-mark"></span>
        <span class="brand-name">Carrington Hill Lodge</span>
      </div>
      <p class="address">BCom, 48 Yarrabee Way, Wattle Downs, Qld 4215.</p>
    </section>

    <section class="card card--back" aria-label="Business card back">
      <div class="back-brand">
        <span class="brand-mark"></span>
        <span class="brand-name">Carrington Hill Lodge</span>
      </div>
    </section>
  </main>
</body>
</html>
```